Website Design Required

Our client needs a website built from scratch. The website is called Snaps4Wall and is essentially a website that allows you to upload a photo, order and pay and your photo is printed onto a canvas. A closely related website is http://www.framelyte.co.za/ however this project needs a clean, fresh design that encourages purchases.

Snaps4wall will be a dedicated website which allows users to upload and print a single image for large format printing.

The website flow will consist of the following:

• A landing page will be designed which showcases the product offering and offers simple and easy to understand instructions on how to get a photo up- loaded and delivered to their door.

• An upload page will exist that allows users the ability to upload a photo to the website for printing.

• Once the user has uploaded a photo the website will ensure that the dimensions are good enough for printing onto canvas and advise the user accordingly if it is not suitable.
• Once the photo has passed this validation we will take the user to a new page that will give them a preview of their photo. Here they will be given a chance to place the photo correctly should the need arise.

• Once the user is happy with the photo placement they will click on the next button which will take them to the payment and delivery page whereby they will need to complete all the fields.

• Once done, a final order page will appear confirming all the details of the order as well as payment and delivery information. Once the user is satisfied he can click the order button.

Requirements
Must have
• We will need the following pages designed:
1. Homepage
2. Upload page
3. Photo placement page (which allows users to align their photo onto the canvas)
4. Order & Payment page
Should not have
• The design should not use old style fonts and shoddy illustrations. If illustrations are used they have to be clean, simple, stylish.

```html
<!DOCTYPE html>
<html lang="en">
<head>
<meta charset="utf-8">
<title>Snaps4Wall – Place your photo</title>
<link href="https://fonts.googleapis.com/css2?family=PT+Sans:wght@400;700&display=swap" rel="stylesheet">
<style>
  :root {
    --page-black: #000000;
    --frame-white: #ffffff;
    --frame-grey: #7f7f7f;
    --sky-top: #a3d1dc;
    --sky-bottom: #ffffff;
    --nav-light: #fbfbfb;
    --nav-dark: #dadada;
    --nav-text: #3a3a3a;
    --tab-dark: #6f6f6f;
    --tab-light: #9a9a9a;
    --ink: #1f1f1f;
    --step-ink: #3d3d3d;
    --step-blue: #1f9fc9;
    --step-blue-dark: #0f7aa3;
    --box-border: #9a9a9a;
    --crop-red: #e3161d;
    --photo-grey: #bdbdbd;
    --card-bg: #eeeeee;
    --smoke: #5a5a5a;
  }
  * { box-sizing: border-box; margin: 0; padding: 0; }
  html, body { width: 1200px; height: 1005px; overflow: hidden; background: var(--page-black); }
  body { position: relative; font-family: "PT Sans", "Helvetica Neue", Arial, sans-serif; }

  .smoke { position: absolute; top: 60px; width: 110px; height: 560px;
    background: radial-gradient(ellipse at center, var(--smoke) 0%, rgba(60,60,60,0.45) 40%, rgba(0,0,0,0) 72%); }
  .smoke--left { left: 0; }
  .smoke--right { right: 0; }

  .site-frame { position: absolute; left: 101px; top: 20px; width: 994px; height: 964px;
    border: 4px solid var(--frame-white); background: var(--frame-grey); }
  .site-page { position: absolute; left: 12px; top: 17px; width: 959px; height: 922px;
    background: linear-gradient(to bottom, var(--sky-top) 0px, var(--sky-bottom) 310px, var(--sky-bottom) 100%); }

  .main-nav { position: absolute; left: 44px; top: 42px; width: 867px; height: 43px; border-radius: 7px;
    background: linear-gradient(to bottom, var(--nav-light), var(--nav-dark));
    box-shadow: 0 1px 2px rgba(0,0,0,0.25); }
  .nav-item { position: absolute; top: 0; height: 43px; line-height: 43px; font-size: 21px;
    color: var(--nav-text); text-align: center; }
  .nav-item--home { left: 10px; top: -5px; width: 151px; height: 46px; line-height: 50px; color: #fff;
    background: linear-gradient(to bottom, var(--tab-light), var(--tab-dark));
    border-radius: 6px 6px 16px 16px; border: 1px dashed rgba(255,255,255,0.6); }
  .nav-item--options { left: 290px; width: 180px; }
  .nav-item--pricing { left: 470px; width: 128px; }
  .nav-item--blog { left: 598px; width: 137px; }
  .nav-item--contact { left: 735px; width: 132px; }
  .nav-divider { position: absolute; top: 6px; width: 1px; height: 31px; background: #c4c4c4; }

  .brand-tag { position: absolute; left: 209px; top: 0; width: 129px; height: 219px; background: #fff;
    box-shadow: 0 2px 4px rgba(0,0,0,0.35); }
  .brand-tag__inner { position: absolute; left: 7px; top: 0; width: 115px; height: 212px;
    background: linear-gradient(to bottom, #5a5a5a 0px, #1a1a1a 110px, #000 111px, #000 100%);
    display: flex; align-items: center; justify-content: center; }
  .brand-name { color: #fff; font-size: 19px; font-weight: 400; }

  .step { position: absolute; left: 517px; top: 133px; }
  .step__icon { position: absolute; left: 0; top: 0; width: 56px; height: 56px; border-radius: 5px;
    background: linear-gradient(to bottom, #48c0e4, var(--step-blue-dark)); }
  .step__title { position: absolute; left: 77px; top: 2px; font-size: 30px; font-weight: 700;
    color: var(--step-ink); line-height: 1; }
  .step__sub { position: absolute; left: 77px; top: 30px; font-size: 20px; white-space: nowrap;
    color: var(--step-ink); }
  .step__number { position: absolute; left: 288px; top: -5px; font-size: 58px; font-weight: 700;
    color: var(--step-ink); line-height: 1; }

  .content-box { position: absolute; left: 41px; top: 203px; width: 870px; height: 654px;
    background: #fff; border: 2px solid var(--box-border); }
  .content-box__heading { position: absolute; left: 38px; top: 78px; font-size: 22px; font-weight: 400;
    color: var(--ink); }

  .photo-stage { position: absolute; left: 104px; top: 146px; width: 661px; height: 440px;
    background: linear-gradient(135deg, #d8d8d8, #9e9e9e 45%, #c9c9c9 70%, #e4e4e4); }
  .crop-area { position: absolute; left: 58px; top: 56px; width: 562px; height: 305px;
    border: 3px solid var(--crop-red);
    background: radial-gradient(ellipse at 45% 45%, #e9c3a0 0%, #d8a886 22%, #7fa6d8 40%, #3f6a3a 65%, #2d4f2a 100%); }
  .move-handle { position: absolute; left: 188px; top: 98px; }

  .payment-cards { position: absolute; left: 387px; top: 871px; display: flex; gap: 8px; }
  .payment-card { width: 41px; height: 31px; border-radius: 3px; background: var(--card-bg);
    border: 1px solid #cfcfcf; font-size: 7px; color: #444; display: flex; align-items: center;
    justify-content: center; }
  .legal-links { position: absolute; left: 0; width: 959px; top: 908px; text-align: center;
    font-size: 11px; color: #111; }
</style>
</head>
<body>
  <div class="smoke smoke--left" role="img" aria-label="Soft grey smoke swirls on black"></div>
  <div class="smoke smoke--right" role="img" aria-label="Soft grey smoke swirls on black"></div>

  <div class="site-frame">
    <div class="site-page">
      <nav class="main-nav">
        <div class="nav-item nav-item--home">Home</div>
        <div class="nav-item nav-item--options">Canvas Options</div>
        <span class="nav-divider" style="left:470px"></span>
        <div class="nav-item nav-item--pricing">Pricing</div>
        <span class="nav-divider" style="left:598px"></span>
        <div class="nav-item nav-item--blog">Blog</div>
        <span class="nav-divider" style="left:735px"></span>
        <div class="nav-item nav-item--contact">Contact</div>
      </nav>

      <div class="brand-tag">
        <div class="brand-tag__inner"><span class="brand-name">Snaps4Wall</span></div>
      </div>

      <div class="step">
        <div class="step__icon">
          <svg width="56" height="56" viewBox="0 0 56 56">
            <path d="M19 12 L19 42 L26 35 L31 46 L36 44 L31 33 L41 33 Z" fill="#fff" stroke="#0f7aa3" stroke-width="1"/>
          </svg>
        </div>
        <div class="step__title">PLACE</div>
        <div class="step__sub">Choose the best place</div>
        <div class="step__number">2</div>
      </div>

      <section class="content-box">
        <h1 class="content-box__heading">Choose the best place to canvas your photo</h1>
        <div class="photo-stage" role="img" aria-label="Greyed family photo of parents, daughter and dog lying on grass">
          <div class="crop-area" role="img" aria-label="Selected canvas area of the photo in full colour">
            <svg class="move-handle" width="52" height="52" viewBox="0 0 52 52">
              <g fill="#fff">
                <rect x="24" y="8" width="4" height="36"/>
                <rect x="8" y="24" width="36" height="4"/>
                <path d="M26 0 L34 10 L18 10 Z"/>
                <path d="M26 52 L34 42 L18 42 Z"/>
                <path d="M0 26 L10 18 L10 34 Z"/>
                <path d="M52 26 L42 18 L42 34 Z"/>
              </g>
            </svg>
          </div>
        </div>
      </section>

      <div class="payment-cards">
        <div class="payment-card">MintCard</div>
        <div class="payment-card">Amberline</div>
        <div class="payment-card">PayPath</div>
        <div class="payment-card">Vela</div>
      </div>
      <div class="legal-links">Terms &amp; Conditions | Privacy Policy</div>
    </div>
  </div>
</body>
</html>
```